Lumo Homes

web design of search platform. Enclosed please find an excel sheet with the info, as well as a picture of a webdesign we like (plumcrate). Idea is to have a modern, inviting website with main colors white, red and dark grey (text). The logo (tavo homes) will be changed to lumo, but you can use this logo for now. Please also use the character enclosed. We can ask this designer to also design the pictograms for the other items, just use something from the net for the design and we'll have it changed afterwards. The texts are enclosed in the word doc enclosed. Thank you!

Target Market(s)

people looking for property in Spain

Industry/Entity Type

Real Estate

Number of Pages Required

1 page

Font styles to use
Other font styles liked:
• a font that goes well with the logo

Colors
ec1f27

Requirements
Must have
• a lot of white
• clean but fun look

```html
<!DOCTYPE html>
<html lang="en">
<head>
<meta charset="utf-8">
<title>Lumo Homes – Estate agents compete, you win</title>
<link rel="stylesheet" href="https://fonts.googleapis.com/css2?family=Montserrat:wght@500;600;700;800&family=Questrial&display=swap">
<style>
  :root {
    --red: #ec1f27;
    --dark: #2b2b2e;
    --text: #4a4a50;
    --muted: #7c7c84;
    --lavender: #efe5fb;
    --lavender-deep: #e6d9f8;
    --soft-grey: #f6f4f6;
    --panel-grey: #f4f4f4;
    --white: #ffffff;
  }
  * { box-sizing: border-box; margin: 0; padding: 0; }
  html, body { width: 1200px; height: 3689px; overflow: hidden; background: var(--white); }
  body { font-family: "Questrial", sans-serif; color: var(--text); }
  .canvas { position: relative; width: 1200px; height: 3689px; overflow: hidden; }
  .abs { position: absolute; }
  h1, h2, h3, .heading { font-family: "Montserrat", sans-serif; color: var(--dark); }

  /* Header */
  .hero-backdrop { left: 0; top: 0; width: 1200px; height: 660px; }
  .brand { left: 58px; top: 48px; font-family: "Montserrat", sans-serif; font-weight: 700; font-size: 64px; letter-spacing: -1px; color: var(--dark); line-height: 1; display: flex; align-items: center; gap: 12px; }
  .brand-dot { width: 14px; height: 14px; border-radius: 50%; background: var(--red); margin-top: 18px; }
  .nav { left: 614px; top: 74px; display: flex; align-items: center; gap: 0; font-size: 17px; color: var(--dark); }
  .nav a { color: inherit; text-decoration: none; margin-right: 36px; }
  .nav .signup { margin-right: 0; background: var(--red); color: var(--white); padding: 7px 14px; border-radius: 8px; }

  /* Hero */
  .hero-title { left: 58px; top: 282px; font-weight: 700; font-size: 44px; line-height: 1.12; letter-spacing: 0.3px; }
  .hero-title .win { background: var(--red); color: var(--white); padding: 0 12px 0 6px; display: inline-block; margin-top: 4px; }
  .hero-copy { left: 58px; top: 389px; width: 570px; font-size: 15px; line-height: 1.45; color: var(--text); }
  .hero-strong { left: 58px; top: 437px; font-size: 14px; font-family: "Montserrat", sans-serif; font-weight: 700; color: var(--dark); }
  .btn-compare { left: 58px; top: 504px; width: 200px; height: 44px; background: var(--dark); color: var(--white); border-radius: 10px; display: flex; align-items: center; font-family: "Montserrat", sans-serif; font-weight: 700; font-size: 13px; overflow: hidden; box-shadow: 0 6px 12px rgba(0,0,0,.18); }
  .btn-compare span { padding-left: 16px; flex: 1; }
  .btn-compare .arrow { width: 40px; height: 44px; background: var(--red); display: flex; align-items: center; justify-content: center; }
  .hero-hint { left: 283px; top: 509px; width: 380px; font-size: 14px; line-height: 1.45; color: var(--muted); }
  .mascot { left: 700px; top: 258px; width: 432px; height: 344px; border-radius: 44% 44% 40% 40%; background: radial-gradient(circle at 50% 42%, #8c8c92 0%, #5a5a60 55%, rgba(90,90,96,0) 72%); }

  /* How it works */
  .section-title { width: 1200px; left: 0; text-align: center; font-weight: 700; font-size: 27px; letter-spacing: 0.3px; }
  .how-title { top: 745px; }
  .step { top: 861px; width: 320px; }
  .step-icon { position: absolute; left: 72px; top: 0; width: 178px; height: 157px; background: var(--red); border-radius: 4px; display: flex; align-items: center; justify-content: center; }
  .step-num { position: absolute; left: 0; top: 116px; font-family: "Montserrat", sans-serif; font-weight: 700; font-size: 44px; color: var(--dark); }
  .step-name { position: absolute; left: 0; top: 172px; font-family: "Montserrat", sans-serif; font-weight: 700; font-size: 25px; line-height: 1.05; color: var(--dark); }
  .step-text { position: absolute; left: 0; top: 239px; width: 262px; font-size: 12.5px; line-height: 1.38; color: var(--muted); }

  /* Compare proposals */
  .proposals { left: 0; top: 1279px; width: 1200px; height: 533px; background: var(--soft-grey); }
  .resume-stack { left: 25px; top: 1335px; width: 415px; height: 428px; }
  .proposals-title { left: 583px; top: 1443px; font-weight: 700; font-size: 33px; line-height: 1.2; }
  .proposals-copy { left: 583px; top: 1545px; width: 560px; font-size: 14.5px; line-height: 1.45; }
  .btn-red { background: var(--red); color: var(--white); font-family: "Montserrat", sans-serif; font-weight: 700; font-size: 14px; border-radius: 12px; display: flex; align-items: center; justify-content: center; box-shadow: 0 6px 12px rgba(236,31,39,.3); }
  .btn-sample { left: 583px; top: 1610px; width: 214px; height: 43px; font-size: 13px; }

  /* Why section */
  .why-label { left: 58px; top: 1905px; font-family: "Montserrat", sans-serif; font-weight: 700; font-size: 40px; color: var(--red); }
  .why-title { left: 58px; top: 1966px; width: 500px; font-weight: 700; font-size: 29px; line-height: 1.2; }
  .btn-viewall { left: 58px; top: 2095px; width: 158px; height: 44px; font-size: 16px; }
  .feature-panel { left: 671px; top: 1906px; width: 358px; height: 186px; background: #f7f7f7; border-radius: 6px; }
  .feature { left: 680px; width: 340px; }
  .feature-icon { position: absolute; left: 4px; top: 2px; width: 52px; height: 56px; border-radius: 8px; }
  .feature-name { position: absolute; left: 72px; top: 0; font-family: "Montserrat", sans-serif; font-weight: 600; font-size: 20px; line-height: 1.25; color: var(--dark); }
  .feature-text { position: absolute; left: 78px; width: 250px; font-size: 14px; line-height: 1.75; color: var(--muted); }

  /* Properties */
  .listings { left: 0; top: 2693px; width: 1200px; height: 996px; background: var(--panel-grey); }
  .listings-title { top: 2778px; font-size: 36px; line-height: 1.25; font-weight: 600; }
  .card { width: 258px; height: 330px; box-shadow: 4px 6px 12px rgba(0,0,0,.28); overflow: hidden; }
  .card-photo { width: 100%; height: 100%; }
  .card-label { position: absolute; left: 12px; bottom: 20px; color: var(--white); font-family: "Montserrat", sans-serif; font-weight: 700; font-size: 13px; line-height: 1.2; }
  .card-go { position: absolute; right: 14px; bottom: 22px; width: 26px; height: 26px; border-radius: 50%; background: var(--red); display: flex; align-items: center; justify-content: center; }
  .tone-a { background: linear-gradient(180deg, #6f6a66 0%, #3e3a36 55%, #2b2d2a 100%); }
  .tone-b { background: linear-gradient(180deg, #d9d6d0 0%, #a9a39a 55%, #6c655c 100%); }
  .tone-c { background: linear-gradient(180deg, #2f2f33 0%, #5a5a60 50%, #8a8a90 100%); }
  .tone-d { background: linear-gradient(180deg, #d4cec8 0%, #8b6f58 55%, #5a3c28 100%); }
</style>
</head>
<body>
<div class="canvas">

  <!-- Header backdrop -->
  <svg class="abs hero-backdrop" viewBox="0 0 1200 660" aria-hidden="true">
    <polygon points="470,0 1200,0 1200,652 700,652" fill="var(--lavender)"/>
    <polygon points="560,0 1200,0 1200,560 820,652 700,652" fill="var(--lavender-deep)" opacity=".45"/>
    <polygon points="760,0 1200,0 1200,300" fill="#ffffff" opacity=".35"/>
  </svg>

  <div class="abs brand">lumo<span class="brand-dot"></span></div>

  <nav class="abs nav">
    <a href="#">Home</a>
    <a href="#">Residential</a>
    <a href="#">Office</a>
    <a href="#">How it Works</a>
    <a href="#" class="signup">Sign up</a>
  </nav>

  <h1 class="abs hero-title">ESTATE AGENTS COMPETE,<br><span class="win">YOU WIN</span></h1>
  <p class="abs hero-copy">Stay anonymous while the estate agents of your choice compete for you by sending you their best proposal, thus guaranteeing you the best deal possible.</p>
  <p class="abs hero-strong">With lumo you will find the best real estate agent for you!</p>

  <a class="abs btn-compare" href="#"><span>COMPARE AGENTS</span>
    <span class="arrow"><svg width="14" height="14" viewBox="0 0 14 14"><path d="M2 7h9M7 3l4 4-4 4" stroke="#fff" stroke-width="2.2" fill="none" stroke-linecap="round" stroke-linejoin="round"/></svg></span>
  </a>
  <p class="abs hero-hint">Enter the city or area where you want to buy or sell compare agents</p>

  <div class="abs mascot" role="img" aria-label="Brand mascot character giving a thumbs up"></div>

  <!-- How it works -->
  <h2 class="abs section-title how-title">HOW LUMO'S FREE SERVICE WORKS</h2>

  <div class="abs step" style="left:59px">
    <div class="step-icon">
      <svg width="110" height="110" viewBox="0 0 110 110" aria-hidden="true">
        <circle cx="46" cy="46" r="30" stroke="#fff" stroke-width="10" fill="none"/>
        <path d="M68 68l26 26" stroke="#fff" stroke-width="12" stroke-linecap="round"/>
      </svg>
    </div>
    <div class="step-num">01.</div>
    <div class="step-name">ENTER YOUR<br>PREFERENCES</div>
    <p class="step-text">Answer a few short questions and, within seconds and at no cost or obligation to you, lumo will filter the best agents for you.</p>
  </div>

  <div class="abs step" style="left:470px">
    <div class="step-icon">
      <svg width="140" height="110" viewBox="0 0 140 110" aria-hidden="true">
        <rect x="8" y="6" width="124" height="98" rx="8" stroke="#fff" stroke-width="6" fill="none"/>
        <line x1="8" y1="26" x2="132" y2="26" stroke="#fff" stroke-width="5"/>
        <circle cx="20" cy="16" r="3" fill="#fff"/><circle cx="30" cy="16" r="3" fill="#fff"/><circle cx="40" cy="16" r="3" fill="#fff"/>
        <polyline points="22,86 42,64 56,78 72,44 88,70 104,50 120,62" stroke="#fff" stroke-width="5" fill="none" stroke-linejoin="round"/>
        <circle cx="42" cy="64" r="5" fill="#fff"/><circle cx="72" cy="44" r="5" fill="#fff"/><circle cx="104" cy="50" r="5" fill="#fff"/>
      </svg>
    </div>
    <div class="step-num">02.</div>
    <div class="step-name">COMPARE<br>PROPOSALS</div>
    <p class="step-text">Answer a few short questions and, within seconds and at no cost or obligation to you, lumo will filter the best agents for you.</p>
  </div>

  <div class="abs step" style="left:883px">
    <div class="step-icon">
      <svg width="130" height="120" viewBox="0 0 130 120" aria-hidden="true">
        <rect x="74" y="8" width="46" height="30" rx="4" stroke="#fff" stroke-width="4" fill="none"/>
        <path d="M84 38l-6 10 14-10" fill="#fff"/>
        <line x1="82" y1="18" x2="112" y2="18" stroke="#fff" stroke-width="3"/>
        <line x1="82" y1="27" x2="104" y2="27" stroke="#fff" stroke-width="3"/>
        <circle cx="52" cy="46" r="18" fill="#fff"/>
        <path d="M18 114c0-28 14-44 34-44s34 16 34 44z" fill="#fff"/>
      </svg>
    </div>
    <div class="step-num">03.</div>
    <div class="step-name">SELECT<br>YOUR AGENT</div>
    <p class="step-text">Answer a few short questions and, within seconds and at no cost or obligation to you, lumo will filter the best agents for you.</p>
  </div>

  <!-- Compare proposals -->
  <section class="abs proposals"></section>
  <svg class="abs resume-stack" viewBox="0 0 415 428" role="img" aria-label="Stack of sample agent proposal sheets">
    <rect x="0" y="0" width="150" height="360" fill="#fbe9b0"/>
    <rect x="72" y="24" width="160" height="380" fill="#f5d56a"/>
    <rect x="72" y="24" width="160" height="380" fill="#fff" opacity=".35"/>
    <rect x="156" y="60" width="258" height="364" fill="#ffffff" stroke="#e4e4e4"/>
    <rect x="156" y="60" width="107" height="364" fill="#f2c21a"/>
    <rect x="263" y="60" width="151" height="364" fill="#fafafa"/>
    <rect x="282" y="96" width="124" height="12" fill="#2b2b2e"/>
    <rect x="282" y="176" width="124" height="12" fill="#2b2b2e"/>
    <rect x="282" y="270" width="124" height="12" fill="#2b2b2e"/>
    <rect x="282" y="336" width="124" height="12" fill="#2b2b2e"/>
    <rect x="168" y="218" width="84" height="12" fill="#2b2b2e"/>
  </svg>

  <h2 class="abs proposals-title">COMPARE PROPOSALS BEFORE<br>SELECTING AN AGENT</h2>
  <p class="abs proposals-copy">Stay anonymous while the estate agents of your choice compete for you by sending you their best proposal, thus guaranteeing you the best deal possible.</p>
  <a class="abs btn-red btn-sample" href="#">VIEW SAMPLE PROPOSAL</a>

  <!-- Why section -->
  <div class="abs why-label">LUMO:</div>
  <h2 class="abs why-title">The smartest way to find the best real estate agent for you simplify your search</h2>
  <a class="abs btn-red btn-viewall" href="#">VIEW ALL</a>

  <div class="abs feature-panel"></div>

  <div class="abs feature" style="top:1928px">
    <div class="feature-icon" role="img" aria-label="Clipboard research pictogram" style="background:linear-gradient(180deg,#f7d46b,#e9a23b)"></div>
    <div class="feature-name">Simplify<br>Your Research</div>
    <p class="feature-text" style="top:66px">lumo simplifies the process of find-ing the best estate agent for you, based on your needs.</p>
  </div>

  <div class="abs feature" style="top:2128px">
    <div class="feature-icon" role="img" aria-label="Target pictogram" style="background:radial-gradient(circle,#ec1f27 0 30%,#fff 31% 50%,#3b7fd4 51% 70%,rgba(0,0,0,0) 71%)"></div>
    <div class="feature-name">Get the best<br>deal</div>
    <p class="feature-text" style="top:66px">lumo simplifies the process of find-ing the best estate agent for you, based on your needs.</p>
  </div>

  <div class="abs feature" style="top:2315px">
    <div class="feature-icon" role="img" aria-label="Group of people pictogram" style="background:linear-gradient(180deg,#9fd0f0,#3f8fd0)"></div>
    <div class="feature-name" style="top:8px">Anonymity</div>
    <p class="feature-text" style="top:48px">lumo simplifies the process of find-ing the best estate agent for you, based on your needs.</p>
  </div>

  <div class="abs feature" style="top:2487px">
    <div class="feature-icon" role="img" aria-label="Coin plant pictogram" style="background:linear-gradient(180deg,#f6d24a,#e08a1e)"></div>
    <div class="feature-name" style="top:8px">100% Free</div>
    <p class="feature-text" style="top:48px">lumo simplifies the process of find-ing the best estate agent for you, based on your needs.</p>
  </div>

  <!-- Properties -->
  <section class="abs listings"></section>
  <h2 class="abs section-title listings-title">NEWLY BUILD PROPERTIES FOR SALE<br>IN SPAIN</h2>

  <article class="abs card" style="left:59px;top:2914px"><div class="card-photo tone-a" role="img" aria-label="Modern villa exterior at dusk"></div><div class="card-label">RANCH TRIANGLE<br>CHICAGO</div><div class="card-go"><svg width="10" height="10" viewBox="0 0 10 10"><path d="M3 1l4 4-4 4" stroke="#fff" stroke-width="2" fill="none"/></svg></div></article>
  <article class="abs card" style="left:330px;top:2914px"><div class="card-photo tone-b" role="img" aria-label="Bright living room with sofa and large windows"></div><div class="card-label">RANCH TRIANGLE<br>CHICAGO</div><div class="card-go"><svg width="10" height="10" viewBox="0 0 10 10"><path d="M3 1l4 4-4 4" stroke="#fff" stroke-width="2" fill="none"/></svg></div></article>
  <article class="abs card" style="left:602px;top:2914px"><div class="card-photo tone-c" role="img" aria-label="Dark modern kitchen with marble island"></div><div class="card-label">RANCH TRIANGLE<br>CHICAGO</div><div class="card-go"><svg width="10" height="10" viewBox="0 0 10 10"><path d="M3 1l4 4-4 4" stroke="#fff" stroke-width="2" fill="none"/></svg></div></article>
  <article class="abs card" style="left:873px;top:2914px"><div class="card-photo tone-d" role="img" aria-label="Wooden kitchen with pendant lights"></div><div class="card-label">RANCH TRIANGLE<br>CHICAGO</div><div class="card-go"><svg width="10" height="10" viewBox="0 0 10 10"><path d="M3 1l4 4-4 4" stroke="#fff" stroke-width="2" fill="none"/></svg></div></article>

  <article class="abs card" style="left:59px;top:3295px"><div class="card-photo tone-a" role="img" aria-label="Modern villa exterior at dusk"></div><div class="card-label">RANCH TRIANGLE<br>CHICAGO</div><div class="card-go"><svg width="10" height="10" viewBox="0 0 10 10"><path d="M3 1l4 4-4 4" stroke="#fff" stroke-width="2" fill="none"/></svg></div></article>
  <article class="abs card" style="left:330px;top:3295px"><div class="card-photo tone-b" role="img" aria-label="Bright living room with sofa and large windows"></div><div class="card-label">RANCH TRIANGLE<br>CHICAGO</div><div class="card-go"><svg width="10" height="10" viewBox="0 0 10 10"><path d="M3 1l4 4-4 4" stroke="#fff" stroke-width="2" fill="none"/></svg></div></article>
  <article class="abs card" style="left:602px;top:3295px"><div class="card-photo tone-c" role="img" aria-label="Dark modern kitchen with marble island"></div><div class="card-label">RANCH TRIANGLE<br>CHICAGO</div><div class="card-go"><svg width="10" height="10" viewBox="0 0 10 10"><path d="M3 1l4 4-4 4" stroke="#fff" stroke-width="2" fill="none"/></svg></div></article>
  <article class="abs card" style="left:873px;top:3295px"><div class="card-photo tone-d" role="img" aria-label="Wooden kitchen with pendant lights"></div><div class="card-label">RANCH TRIANGLE<br>CHICAGO</div><div class="card-go"><svg width="10" height="10" viewBox="0 0 10 10"><path d="M3 1l4 4-4 4" stroke="#fff" stroke-width="2" fill="none"/></svg></div></article>

</div>
</body>
</html>
```